Website for Nonprofit for kids whose parents have been wounded

We need a web design for a nonprofit that serves children who have been severely burned as well as those whose parents have been wounded during military service. We will be based out of hospitals and will need a format that will encourage trust, safety, and respect. We are stick with a lot of red white and blue. We will also be looking to have a space for donations.

Target Market(s)

Kids and parents of military veterans

Industry/Entity Type

Non Profit

Number of Pages Required

5+ page

Font styles to use
Serif
Decorative

Colors
ec1f27
ffffff
0255a3

Requirements
Must have
• Be both appealing to children and adults. Create a reputable face for our organization. We need an area for donations.
Nice to have
• Something unique

```html
<!DOCTYPE html>
<html lang="en">
<head>
<meta charset="utf-8">
<title>Harbor Kids</title>
<link href="https://fonts.googleapis.com/css2?family=Open+Sans:wght@400;600;700;800&display=swap" rel="stylesheet">
<style>
:root{
  --red:#e3262d;
  --blue:#0255a3;
  --sky:#2a9fdc;
  --ink:#333;
  --muted:#777;
  --dark:#3a3a3a;
  --darker:#2b2b2b;
  --footer:#303236;
  --field:#4a4c50;
  --white:#fff;
}
*{box-sizing:border-box;margin:0;padding:0}
html,body{width:1200px;height:2368px;overflow:hidden}
body{font-family:"Open Sans",Arial,sans-serif;color:var(--ink);background:var(--white);font-size:13px;line-height:1.5}
.site-header{height:120px;position:relative;border-top:4px solid #d8d8d8}
.brand{position:absolute;left:60px;top:22px;display:flex;align-items:center;gap:12px}
.brand-dot{width:44px;height:44px;border-radius:50%;background:var(--blue)}
.brand-name{font-size:26px;font-weight:700;color:var(--blue);letter-spacing:1px}
.main-nav{position:absolute;right:60px;top:0;display:flex}
.main-nav a{display:block;padding:20px 20px 16px;font-size:14px;color:#555;text-decoration:none}
.main-nav a.active{background:var(--sky);color:var(--white)}
.contact-strip{position:absolute;right:60px;top:70px;text-align:right;font-size:12px;color:#666;line-height:1.5}
.hero{background:var(--dark);height:520px;position:relative;text-align:center;color:var(--white)}
.hero h1{font-size:38px;font-weight:700;padding-top:18px;letter-spacing:.5px}
.hero .lead{font-size:17px;margin-top:2px}
.slide{position:absolute;left:160px;top:130px;width:880px;height:332px;background:linear-gradient(135deg,#8d97a3,#c9cdd2 45%,#5b6b82)}
.slide-caption{position:absolute;left:0;right:0;bottom:0;height:36px;background:rgba(0,0,0,.55);font-size:12px;line-height:36px;text-align:left;padding-left:20px}
.slider-dots{position:absolute;left:0;right:0;top:484px;display:flex;justify-content:center;gap:10px}
.slider-dots span{width:11px;height:11px;border-radius:50%;background:#aaa}
.slider-dots span.on{background:var(--white)}
.welcome{height:520px;text-align:center;padding-top:36px}
.section-title{display:flex;align-items:center;justify-content:center;gap:24px;font-size:34px;font-weight:700;color:var(--red)}
.section-title::before,.section-title::after{content:"";width:200px;height:2px;background:var(--red)}
.intro{font-size:13px;color:#444;margin-top:8px}
.features{display:flex;justify-content:center;gap:70px;margin-top:40px}
.feature{width:190px}
.feature-icon{width:60px;height:60px;border-radius:50%;border:2px solid #999;margin:0 auto;display:flex;align-items:center;justify-content:center}
.feature h3{font-size:15px;font-weight:600;margin-top:14px;color:#333}
.feature p{font-size:12px;color:var(--muted);margin-top:10px}
.btn{display:inline-block;margin-top:18px;padding:6px 16px;border:1px solid #bbb;font-size:12px;color:#444;border-radius:3px}
.btn.primary{background:var(--blue);border-color:var(--blue);color:var(--white)}
.services{height:560px;background:linear-gradient(100deg,#4a2818,#6e3a22 45%,#2c1f1a);text-align:center;color:var(--white);padding-top:36px}
.services h2{font-size:32px;font-weight:700}
.services .intro{color:#eee}
.cards{display:flex;justify-content:center;gap:40px;margin-top:30px}
.card{width:210px;height:350px;background:var(--white);color:var(--ink);padding:20px 18px;border-radius:2px}
.card-photo{width:100px;height:100px;border-radius:50%;margin:0 auto;background:linear-gradient(135deg,#d9b9a0,#8c6b58)}
.card h3{font-size:14px;color:var(--red);font-weight:700;margin-top:24px}
.card p{font-size:12px;color:var(--muted);margin-top:10px}
.card-more{width:26px;height:26px;border-radius:50%;border:2px solid #555;margin:20px auto 0;display:flex;align-items:center;justify-content:center}
.team{height:400px;text-align:center;padding-top:24px;overflow:hidden}
.team h2{font-size:32px;font-weight:700;color:#333;line-height:1.4}
.members{display:flex;justify-content:center;gap:50px;margin-top:20px}
.member{width:220px;text-align:left}
.member-photo{width:160px;height:160px;margin:0 auto;border-radius:50% 50% 8px 8px;background:linear-gradient(180deg,#e8d2bf,#c7a88f)}
.member h3{font-size:15px;font-weight:600;margin-top:10px}
.member p{font-size:12px;color:var(--muted);margin-top:4px}
.member .profile{display:block;text-align:right;color:var(--red);font-size:12px;margin-top:4px}
.site-footer{position:relative;height:248px;background:var(--footer);color:#bbb}
.footer-cols{display:flex;gap:90px;padding:22px 0 0 120px}
.footer-col{width:260px;font-size:11px;line-height:1.5}
.footer-col h4{color:var(--white);font-size:13px;font-weight:700;margin-bottom:10px;text-transform:uppercase}
.footer-col .address{margin-top:8px}
.footer-col ul{list-style:none}
.footer-col li{color:var(--red);line-height:1.9}
.field{height:24px;background:var(--field);margin-bottom:8px}
.field.tall{height:56px}
.submit{display:inline-block;background:var(--blue);color:var(--white);font-size:11px;padding:3px 12px}
.copyright{position:absolute;left:0;right:0;bottom:0;height:30px;line-height:30px;text-align:center;background:var(--darker);font-size:11px;color:#999}
</style>
</head>
<body>
<header class="site-header">
  <div class="brand"><span class="brand-dot"></span><span class="brand-name">Harbor Kids</span></div>
  <nav class="main-nav">
    <a class="active" href="#">Home</a><a href="#">About Us</a><a href="#">Services</a><a href="#">Donations</a><a href="#">Blog</a><a href="#">Contact Us</a>
  </nav>
  <div class="contact-strip">Email Us : hello@harborkids.org<br>Call : (555) 014-2290</div>
</header>

<section class="hero">
  <h1>IN FRINGILLA MASSA UT NISI ULLAMCORPER</h1>
  <p class="lead">Lorem ipsum dolor sit amet, consectetur adipiscing elit. Nunc non diam erat.</p>
  <div class="slide" role="img" aria-label="Photo of a child embracing a parent in uniform">
    <div class="slide-caption">Brave families deserve gentle care, safe spaces and a community that stands beside them every day.</div>
  </div>
  <div class="slider-dots"><span class="on"></span><span></span><span></span><span></span><span></span></div>
</section>

<section class="welcome">
  <h2 class="section-title">WELCOME !</h2>
  <p class="intro">Lorem Ipsum is simply dummy text of the printing and typesetting industry.<br>Lorem Ipsum has been the industry's standard dummy.</p>
  <div class="features">
    <div class="feature">
      <div class="feature-icon"><svg width="28" height="28" viewBox="0 0 28 28"><path d="M14 24 4 14a5 5 0 0 1 10-6 5 5 0 0 1 10 6z" fill="none" stroke="#777" stroke-width="2"/></svg></div>
      <h3>Lorem Ipsum is simply</h3>
      <p>Lorem Ipsum is simply dummy text of the printing and typesetting industry. Lorem Ipsum has been the industry's.</p>
      <span class="btn primary">Read More</span>
    </div>
    <div class="feature">
      <div class="feature-icon"><svg width="28" height="28" viewBox="0 0 28 28"><circle cx="14" cy="14" r="10" fill="none" stroke="#777" stroke-width="2"/><path d="M9 14l4 4 7-8" fill="none" stroke="#777" stroke-width="2"/></svg></div>
      <h3>Lorem Ipsum is simply</h3>
      <p>Lorem Ipsum is simply dummy text of the printing and typesetting industry. Lorem Ipsum has been the industry's.</p>
      <span class="btn">Read More</span>
    </div>
    <div class="feature">
      <div class="feature-icon"><svg width="28" height="28" viewBox="0 0 28 28"><circle cx="10" cy="10" r="4" fill="#777"/><circle cx="19" cy="10" r="4" fill="#777"/><path d="M3 23a7 7 0 0 1 14 0M12 23a7 7 0 0 1 14 0" fill="#777"/></svg></div>
      <h3>Lorem Ipsum is simply</h3>
      <p>Lorem Ipsum is simply dummy text of the printing and typesetting industry. Lorem Ipsum has been the industry's.</p>
      <span class="btn">Read More</span>
    </div>
    <div class="feature">
      <div class="feature-icon"><svg width="28" height="28" viewBox="0 0 28 28"><circle cx="14" cy="14" r="5" fill="none" stroke="#777" stroke-width="2"/><circle cx="14" cy="14" r="10" fill="none" stroke="#777" stroke-width="2" stroke-dasharray="4 3"/></svg></div>
      <h3>Lorem Ipsum is simply</h3>
      <p>Lorem Ipsum is simply dummy text of the printing and typesetting industry. Lorem Ipsum has been the industry's.</p>
      <span class="btn">Read More</span>
    </div>
  </div>
</section>

<section class="services" role="img" aria-label="Background photo of a child with a caring adult">
  <h2>WHAT WE DO ?</h2>
  <p class="intro">Lorem Ipsum is simply dummy text of the printing and typesetting industry.<br>Lorem Ipsum has been the industry's standard dummy.</p>
  <div class="cards">
    <div class="card"><div class="card-photo" role="img" aria-label="Portrait of a smiling child"></div><h3>Lorem Ipsum is simply</h3><p>Lorem Ipsum is simply dummy text of the printing and typesetting industry. Lorem Ipsum has been the industry's.</p><div class="card-more"><svg width="12" height="12" viewBox="0 0 12 12"><path d="M4 2l4 4-4 4" fill="none" stroke="#555" stroke-width="2"/></svg></div></div>
    <div class="card"><div class="card-photo" role="img" aria-label="Portrait of two children together"></div><h3>Lorem Ipsum is simply</h3><p>Lorem Ipsum is simply dummy text of the printing and typesetting industry. Lorem Ipsum has been the industry's.</p><div class="card-more"><svg width="12" height="12" viewBox="0 0 12 12"><path d="M4 2l4 4-4 4" fill="none" stroke="#555" stroke-width="2"/></svg></div></div>
    <div class="card"><div class="card-photo" role="img" aria-label="Portrait of a young boy"></div><h3>Lorem Ipsum is simply</h3><p>Lorem Ipsum is simply dummy text of the printing and typesetting industry. Lorem Ipsum has been the industry's.</p><div class="card-more"><svg width="12" height="12" viewBox="0 0 12 12"><path d="M4 2l4 4-4 4" fill="none" stroke="#555" stroke-width="2"/></svg></div></div>
    <div class="card"><div class="card-photo" role="img" aria-label="Portrait of a happy child"></div><h3>Lorem Ipsum is simply</h3><p>Lorem Ipsum is simply dummy text of the printing and typesetting industry. Lorem Ipsum has been the industry's.</p><div class="card-more"><svg width="12" height="12" viewBox="0 0 12 12"><path d="M4 2l4 4-4 4" fill="none" stroke="#555" stroke-width="2"/></svg></div></div>
  </div>
</section>

<section class="team">
  <h2>MEET OUR TEAM</h2>
  <div class="members">
    <div class="member"><div class="member-photo" role="img" aria-label="Portrait of team member Clara"></div><h3>Clara</h3><p>Lorem ipsum dolor sit amet, consectetur adipiscing elit. Sed quis nisl vel augue dictum porta.</p><span class="profile">View Profile »</span></div>
    <div class="member"><div class="member-photo" role="img" aria-label="Portrait of team member Owen"></div><h3>Owen</h3><p>Lorem ipsum dolor sit amet, consectetur adipiscing elit. Sed quis nisl vel augue dictum porta.</p><span class="profile">View Profile »</span></div>
    <div class="member"><div class="member-photo" role="img" aria-label="Portrait of team member Peter"></div><h3>Peter</h3><p>Lorem ipsum dolor sit amet, consectetur adipiscing elit. Sed quis nisl vel augue dictum porta.</p><span class="profile">View Profile »</span></div>
    <div class="member"><div class="member-photo" role="img" aria-label="Portrait of team member Nora"></div><h3>Nora</h3><p>Lorem ipsum dolor sit amet, consectetur adipiscing elit. Sed quis nisl vel augue dictum porta.</p><span class="profile">View Profile »</span></div>
  </div>
</section>

<footer class="site-footer">
  <div class="footer-cols">
    <div class="footer-col">
      <h4>Company Details</h4>
      <p>Caring for children of wounded service members through hospital programs, play and family support.</p>
      <p class="address">Harbor Kids<br>200 Example Avenue<br>Springfield<br>Phone: (555) 014-2290<br>Email: hello@harborkids.org</p>
    </div>
    <div class="footer-col">
      <h4>Quick Links</h4>
      <ul><li>Lorem ipsum dolor sit</li><li>Consectetur adipiscing</li><li>Sed quis nisl augue</li><li>Dictum porta sed nibh</li><li>Vivamus in tellus</li><li>Donate to our cause</li></ul>
    </div>
    <div class="footer-col">
      <h4>Contact Us</h4>
      <div class="field"></div><div class="field"></div><div class="field tall"></div>
      <span class="submit">SUBMIT</span>
    </div>
  </div>
  <div class="copyright">Copyright © 2024 Harbor Kids. All Rights Reserved.</div>
</footer>
</body>
</html>
```